copper lantern website

We need a new website for our new business division. We are a sustainable design firm specializing in servicing the needs if architects and developers. We have a staff consisting of architects, engineers, and former contractors and we understand green must make sense.

Bottomline - the only sustainable and copper lantern solutions are those thatbare good for the environment and good for our clients bottom line.

Our company is copper lantern and we will send you a copy of our logo you will see our tagline. Is simple. sustainable. solutions. The play with the periods is that we believe their are simple sustainable solutions and we want to use the words together and possible let each stand alone to accentuate their individual meaning in regards to benefit to our clients.

We want a cool splash page with nich graphics and pictures then later pages to feature projects and design ideas.

Target Market(s)

Our target customers are architects, developers, and contractors who would need assistance with the design process for a VARN project or assisatnce with a building owner who wants to make tehir facilty more environmentally friendly and save energy costs at the same tiem.

Industry/Entity Type

Environment

Requirements
Must have
• Needs a construction look with an environmentally friendly surrounding that is pleasing to look at. Must appeal to the client not only as environmentally friendly but also a wise investment.
Nice to have
• Opportunity for a connection to Social networking including a blog.
Should not have
• A totally environmental building feel at whatever cost. We want to emphasize that it is possible to build environmental friendly and save you money over the life of your building

```html
<!DOCTYPE html>
<html lang="en">
<head>
<meta charset="utf-8">
<title>copper lantern — Architechture</title>
<link rel="stylesheet" href="https://fonts.googleapis.com/css2?family=Arimo:wght@400;700&family=Cinzel:wght@700&family=Jura:wght@500&family=Michroma&display=swap">
<style>
  :root {
    --page-bg: #e2e2e2;
    --page-light: #f4f4f4;
    --bar-black: #111111;
    --nav-cream: #f1e2b3;
    --tab-blue: #17358a;
    --tab-active-text: #2c3b6b;
    --tab-active-bg: #efefef;
    --band-green: #4aa51b;
    --band-green-dark: #2f8a0e;
    --card-black: #000000;
    --card-text: #b9b9b9;
    --card-title: #f2f2f2;
    --brand-grey: #555555;
    --swirl-green: #1f8a3a;
  }
  * { box-sizing: border-box; margin: 0; padding: 0; }
  html, body { width: 1200px; height: 900px; overflow: hidden; }
  body {
    position: relative;
    background: radial-gradient(ellipse at 62% 45%, var(--page-light) 0%, var(--page-bg) 60%, #d8d8d8 100%);
    font-family: "Arimo", Arial, sans-serif;
  }
  .vine-ornament {
    position: absolute; left: 0; top: 0; width: 240px; height: 265px;
    background: radial-gradient(ellipse at 40% 40%, rgba(90,160,60,.28), rgba(90,160,60,0) 70%);
  }
  .ribbon-swirl {
    position: absolute; right: 0; top: 0; width: 200px; height: 900px;
    background: linear-gradient(100deg, rgba(255,255,255,0) 0%, rgba(130,210,150,.45) 35%, var(--swirl-green) 70%, #0f5a22 100%);
  }
  .login-tab {
    position: absolute; left: 35px; top: 0; width: 253px; height: 48px;
    background: var(--bar-black); border-radius: 0 0 8px 8px;
    display: flex; align-items: center; padding-left: 9px; gap: 8px;
  }
  .social-square { width: 27px; height: 27px; border-radius: 3px; background: #5aa8dd; }
  .social-square.second { background: #3b5a9a; }
  .login-tab a {
    margin-left: 16px; font-family: "Cinzel", serif; font-weight: 700; font-size: 18px;
    color: var(--nav-cream); text-decoration: none; letter-spacing: .5px;
  }
  .main-nav {
    position: absolute; left: 364px; top: 0; width: 815px; height: 56px;
    background: linear-gradient(#222, var(--bar-black)); border-radius: 0 0 8px 8px;
  }
  .main-nav a {
    position: absolute; top: 15px; font-family: "Cinzel", serif; font-weight: 700; font-size: 18px;
    color: var(--nav-cream); text-decoration: none; letter-spacing: .8px;
  }
  .nav-pointer { position: absolute; left: 430px; top: 55px; }
  .section-tabs a {
    position: absolute; top: 202px; font-family: "Michroma", sans-serif; font-size: 23px;
    color: var(--tab-blue); text-decoration: none; letter-spacing: -.5px; -webkit-text-stroke: .6px var(--tab-blue);
  }
  .section-tabs .active {
    left: 592px; top: 185px; width: 273px; height: 72px; background: var(--tab-active-bg);
    color: var(--tab-active-text); -webkit-text-stroke: .6px var(--tab-active-text); border-radius: 4px 4px 0 0;
    display: flex; align-items: center; justify-content: center;
  }
  .project-band {
    position: absolute; left: 0; top: 320px; width: 970px; height: 460px;
    background: linear-gradient(180deg, #5cb425, var(--band-green) 50%, var(--band-green-dark));
  }
  .pager-band {
    position: absolute; left: 608px; top: 770px; width: 362px; height: 57px; background: var(--band-green-dark);
  }
  .project-card {
    position: absolute; top: 341px; width: 312px; height: 414px; background: var(--card-black);
  }
  .project-photo { position: absolute; left: 6px; top: 14px; width: 300px; height: 213px; }
  .project-title {
    position: absolute; left: 6px; top: 236px; font-family: "Jura", sans-serif; font-size: 25px; font-weight: 500;
    color: var(--card-title); letter-spacing: 1px;
  }
  .project-category {
    position: absolute; right: 30px; top: 252px; font-size: 10px; font-weight: 700; color: var(--card-text);
  }
  .project-summary {
    position: absolute; left: 22px; right: 22px; top: 278px; text-align: center;
    font-size: 13.5px; line-height: 23px; color: var(--card-text);
  }
  .read-more {
    position: absolute; right: 30px; top: 385px; font-size: 10.5px; font-weight: 700; color: var(--card-text); text-decoration: none;
  }
  .pager-button {
    position: absolute; top: 782px; height: 27px; background: var(--card-black);
    color: #ccc; font-size: 10px; font-weight: 700; display: flex; align-items: center; justify-content: center; text-decoration: none;
  }
  .pager-pages {
    position: absolute; left: 733px; top: 789px; font-family: "Michroma", sans-serif; font-size: 10px; color: #000; letter-spacing: 1px;
  }
  .brand {
    position: absolute; left: 22px; top: 814px;
    font-size: 40px; color: var(--brand-grey); line-height: 44px;
  }
</style>
</head>
<body>
  <div class="vine-ornament" role="img" aria-label="Curling green vine with leaves"></div>
  <div class="ribbon-swirl" role="img" aria-label="Flowing green and white ribbon swirls"></div>

  <div class="login-tab">
    <span class="social-square" aria-label="Microblog"></span>
    <span class="social-square second" aria-label="Social network"></span>
    <a href="#">USER LOGIN</a>
  </div>

  <nav class="main-nav">
    <a href="#" style="left:46px">HOME</a>
    <a href="#" style="left:204px">ABOUT US</a>
    <a href="#" style="left:421px">BLOG</a>
    <a href="#" style="left:585px">CONTACT US</a>
  </nav>
  <svg class="nav-pointer" width="26" height="16" viewBox="0 0 26 16"><path d="M0 0 H26 L13 15 Z" fill="#111"/></svg>

  <div class="section-tabs">
    <a href="#" style="left:140px">contractors</a>
    <a href="#" style="left:375px">engineering</a>
    <a href="#" class="active">architechture</a>
  </div>

  <div class="project-band"></div>
  <div class="pager-band"></div>

  <article class="project-card" style="left:0">
    <div class="project-photo" role="img" aria-label="Modern white house with a concrete annex on a lawn" style="background:linear-gradient(160deg,#dfe6e8,#8e9a92 50%,#3f6a2a)"></div>
    <h2 class="project-title">Dawn</h2>
    <span class="project-category">Architechture</span>
    <p class="project-summary">One of our best designs. Situated in texas, is full of natural lighting &amp; fresh air. With solar water heater &amp; power generation.</p>
    <a class="read-more" href="#">Read More</a>
  </article>

  <article class="project-card" style="left:320px">
    <div class="project-photo" style="left:8px;width:296px;background:linear-gradient(170deg,#1c3c7a,#2d3440 45%,#7a5a3a 75%,#5a4a3a)" role="img" aria-label="Lit timber and glass house at dusk"></div>
    <h2 class="project-title" style="left:18px">Pine</h2>
    <span class="project-category" style="right:26px">Architechture</span>
    <p class="project-summary">One of our best designs. Situated in texas, is full of natural lighting &amp; fresh air. With solar water heater &amp; power generation.</p>
    <a class="read-more" href="#" style="right:26px">Read More</a>
  </article>

  <article class="project-card" style="left:640px">
    <div class="project-photo" style="left:9px;width:295px;background:linear-gradient(180deg,#5a8ee0,#c9d7e6 45%,#d8dcdc 65%,#3d7a2a)" role="img" aria-label="Round white futuristic house among trees"></div>
    <h2 class="project-title" style="left:15px;top:232px">Eclipse</h2>
    <span class="project-category" style="right:25px;top:247px">Engineering</span>
    <p class="project-summary" style="top:276px">One of our best designs. Situated in texas, is full of natural lighting &amp; fresh air. With solar water heater &amp; power generation.</p>
    <a class="read-more" href="#" style="top:383px;right:25px">Read More</a>
  </article>

  <a class="pager-button" href="#" style="left:637px;width:94px">Previous</a>
  <span class="pager-pages">1 2 3 and 46</span>
  <a class="pager-button" href="#" style="left:825px;width:93px">Next</a>

  <div class="brand">copper lantern</div>
</body>
</html>
```